Investment Opportunities

* Need a one page full colour flyer 8.5 inches by 11 inches printed on two sides
* Must be visually appealing using earth tone colours that compliment the logo color
* use creative graphics and icons to support the message

Target Market(s)

investors

Industry/Entity Type

nutraceuticals

```html
<!DOCTYPE html>
<html lang="en">
<head>
<meta charset="utf-8">
<title>NutriVance Inc. – Business Plan Overview Flyer</title>
<link href="https://fonts.googleapis.com/css2?family=Montserrat:wght@400;500;600;700&family=Cinzel:wght@500;600&display=swap" rel="stylesheet">
<style>
:root{
  --teal:#14a38a;
  --teal-dark:#0f8a74;
  --red:#ec2227;
  --ink:#222;
  --paper:#ffffff;
  --paper-grey:#f1f2f3;
  --backdrop:#e4e5e7;
}
*{box-sizing:border-box;margin:0;padding:0}
html,body{width:900px;height:1200px;overflow:hidden}
body{background:var(--backdrop);font-family:'Montserrat',sans-serif;color:var(--ink);position:relative}
.page{position:absolute;top:322px;width:430px;height:556px;background:var(--paper);overflow:hidden;box-shadow:0 4px 14px rgba(0,0,0,.18)}
.page--front{left:12px}
.page--back{left:458px;background:linear-gradient(180deg,var(--paper-grey),#fff 40%)}
.abs{position:absolute}

/* front */
.hero-photo{left:0;top:0;width:430px;height:270px;background:linear-gradient(180deg,#9c7a4e 0%,#c9b08a 35%,#e9e2d6 70%,#fff 100%)}
.brand{left:0;top:118px;width:430px;display:flex;align-items:center;justify-content:center;gap:8px}
.brand__dot{width:18px;height:18px;border-radius:50%;background:var(--teal)}
.brand__name{font-family:'Montserrat',sans-serif;font-weight:700;font-size:26px;color:var(--teal)}
.overview{left:14px;top:235px;width:174px;height:264px;background:var(--teal);border-radius:4px;color:#fff;padding:18px 8px 0 9px;font-size:7px;line-height:1.4}
.overview h2{font-size:8.6px;font-weight:600;line-height:1.15;margin-bottom:10px}
.overview p{margin-bottom:9px}
.overview b{font-weight:600}
.overview .stmt{display:flex;gap:4px}
.overview .stmt i{flex:0 0 10px;height:10px;border:1px solid #fff;border-radius:50%;margin-top:1px}
.side-strip{left:404px;top:235px;width:12px;height:264px;background:var(--teal);border-radius:0 4px 4px 0}
.card{left:188px;top:195px;width:216px;height:361px;background:#fff;border-radius:8px 8px 0 0;box-shadow:0 0 6px rgba(0,0,0,.12);padding:11px 10px 0 11px;font-size:6.6px;line-height:1.38}
.card__title{font-family:'Cinzel',serif;font-weight:600;color:var(--teal);font-size:15px;text-align:center}
.card__sub{font-family:'Cinzel',serif;color:var(--red);font-size:9.4px;text-align:center;line-height:1.25;margin-bottom:9px}
.tag{display:flex;align-items:center;margin:0 0 10px -8px}
.tag__icon{width:30px;height:30px;border-radius:50%;border:1.5px solid var(--red);background:#fff;display:flex;align-items:center;justify-content:center;position:relative;z-index:1}
.tag__label{background:var(--red);color:#fff;font-weight:600;font-size:8.2px;padding:2px 14px 2px 8px;border-radius:0 8px 8px 0;margin-left:-2px;width:140px}
.card h4{font-size:7px;font-weight:700;margin:6px 0 3px 7px}
.card ol{list-style:none;margin-left:7px}
.card li{padding-left:8px;text-indent:-8px;margin-bottom:6px}
.card .tight li{margin-bottom:0}

/* back */
.pill{background:var(--teal);color:#fff;font-weight:600;border-radius:8px;padding:1px 12px}
.team-pill{left:13px;top:24px;width:139px;font-size:9.2px}
.extra-box{left:330px;top:0;width:92px;height:110px;background:var(--red);border-radius:0 0 8px 8px;color:#fff;font-weight:600;font-size:10.2px;line-height:1.6;text-align:center;padding-top:20px}
.team-intro{left:25px;top:47px;width:300px;font-size:6.6px;line-height:1.3}
.member{top:80px;width:100px;text-align:center;font-size:5.4px;line-height:1.3}
.member__photo{width:47px;height:64px;margin:0 auto 4px}
.member__name{color:var(--red);font-weight:700;font-size:6.6px}
.market{left:12px;top:187px;width:230px;height:369px;background:var(--teal);border-radius:8px 8px 0 0;color:#fff;padding:17px 10px 0 10px;font-size:6.5px;line-height:1.32}
.market h3{font-size:8.2px;font-weight:600;margin-bottom:4px}
.market ul,.plan ul{list-style:none}
.market li,.plan li{padding-left:7px;text-indent:-6px;margin-bottom:7px}
.market li::before,.plan li::before{content:"•";margin-right:3px}
.market li.sub{padding-left:15px}
.market li.sub::before{content:"i.";}
.plan{left:253px;top:198px;width:172px;font-size:6.5px;line-height:1.32}
.plan .tag{margin:0 0 7px 0}
.plan .tag__label{width:92px;font-size:8px;padding-left:7px}
.plan .tag__icon{width:30px;height:30px}
.plan li{margin-bottom:6px}
.money{color:var(--red);font-weight:700}
.fin{margin-top:10px}
.fin li{margin-bottom:4px}
.contact{left:242px;top:476px;width:188px;height:64px;background:var(--red);color:#fff;text-align:center;font-size:6.6px;line-height:1.42;padding-top:5px;font-weight:600}
.contact__name{font-size:7.8px}
.contact__name small{font-size:6.4px;font-weight:500}
.contact__phone{font-size:14px;font-weight:700;margin-top:2px}
.request{left:242px;top:540px;width:188px;height:10px;background:var(--teal);color:#fff;font-size:6.3px;text-align:center;line-height:10px}
</style>
</head>
<body>

<section class="page page--front">
  <div class="abs hero-photo" role="img" aria-label="Photo of business people reviewing charts and documents at a desk"></div>
  <div class="abs brand">
    <span class="brand__dot"></span>
    <span class="brand__name">NutriVance</span>
  </div>

  <div class="abs overview">
    <h2>NutriVance Company<br>Overview</h2>
    <p>&nbsp;• The <b>goal of NutriVance Inc.</b> is to enhance human and animal health through immune-focused testing, manufacturing, and promoting immunoceutical products that aid in the prevention and treatment of infectious diseases and cancers by naturally enhancing immunity.</p>
    <p class="stmt"><i></i><span><b>Vision Statement:</b> To educate, empower and equip the global community to achieve health &amp; wellbeing more naturally.</span></p>
    <p class="stmt"><i></i><span><b>Mission Statement:</b> To provide research, resources, laboratory services and immunoceutical products that improve the health of all living beings.</span></p>
    <p class="stmt"><i></i><span><b>Values:</b> Evidence-based research, Innovation, Integrity, Transparency, Team-centred, and Education</span></p>
  </div>
  <div class="abs side-strip"></div>

  <div class="abs card">
    <div class="card__title">NutriVance Inc.</div>
    <div class="card__sub">Business Plan Overview<br>Spring 2022</div>
    <div class="tag">
      <span class="tag__icon"><svg width="16" height="14" viewBox="0 0 16 14" fill="none" stroke="#ec2227" stroke-width="1.1"><circle cx="4" cy="4" r="1.6"/><path d="M1.5 13V8h5v5"/><circle cx="11" cy="4" r="2.4"/><path d="M11 2.8v2.4M8 13V9h6v4"/></svg></span>
      <span class="tag__label">Investment Opportunity</span>
    </div>
    <h4>Problem/opportunity:</h4>
    <ol>
      <li>i.&nbsp; Infectious disease, cancers, autoimmune disorders, inflammatory conditions, and allergies are increasing, affecting both human and animal populations.</li>
      <li>ii.&nbsp; There is a significant and growing need for innovative healthful products and services focused on these areas of concern.</li>
    </ol>
    <h4>Solution:</h4>
    <ol>
      <li>i.&nbsp; Immunoceuticals are one of the emerging treatment options that would address the current unmet need in a more natural manner.</li>
      <li>ii. NutriVance Inc. is poised to become the premier provider of research, resources, services and products to take advantage of these growing global market opportunities.</li>
    </ol>
    <h4>Investment opportunity:</h4>
    <ol class="tight">
      <li>i.&nbsp; 1000 shares at $1000 per share (total: $1M)</li>
      <li>ii. Start-up date target: July 1, 2022</li>
    </ol>
  </div>
</section>

<section class="page page--back">
  <div class="abs pill team-pill">The Scientific Team</div>
  <div class="abs extra-box">PLUS THREE<br>ADDITIONAL<br>SUPPORTING<br>SCIENTISTS</div>
  <p class="abs team-intro">A core group of highly credentialed, award-winning scientists have been assembled. The three principal scientists leading this company are:</p>

  <div class="abs member" style="left:17px">
    <div class="member__photo" role="img" aria-label="Portrait photo of Dr. Aaron Fields" style="background:linear-gradient(180deg,#bfc3c6,#d9383c)"></div>
    <div class="member__name">Dr. Aaron Fields</div>
    (Professor of Viral Immunology<br>and Cancer Biology)
  </div>
  <div class="abs member" style="left:121px">
    <div class="member__photo" role="img" aria-label="Portrait photo of Dr. Peter Lindqvist" style="background:linear-gradient(180deg,#3b82c4,#a39c8c)"></div>
    <div class="member__name">Dr. Peter Lindqvist</div>
    (Professor of Immuno-Toxicology<br>and Nutritional Immunology)
  </div>
  <div class="abs member" style="left:222px">
    <div class="member__photo" role="img" aria-label="Portrait photo of Dr. Claire Whitmore" style="background:linear-gradient(180deg,#6e5448,#2c2420)"></div>
    <div class="member__name">Dr. Claire Whitmore</div>
    Professor of Immunology and<br>Immunogenetics
  </div>

  <div class="abs market">
    <h3>Market Potential</h3>
    <ul>
      <li>Infectious disease, cancers, autoimmune disorders, inflammatory conditions and allergies are increasing, affecting both human and animal populations.</li>
      <li>Current treatments are proving somewhat ineffective. A properly functioning immune system is the key and common thread that helps to keep the body healthy and free of various disorders.</li>
      <li>There is increased public awareness regarding new prevention and treatment strategies that rely on more natural approaches to improve human and animal wellbeing.</li>
      <li>The solution to these challenges includes developing novel innovative health solutions and products to meet the need.</li>
      <li>Immunoceuticals are one of the emerging treatment options that would address the current unmet need.</li>
      <li class="sub"> “Immunoceuticals” is a novel term, which means immunological products and systems that naturally improve immuno-competence of an individual.</li>
      <li>The immunoceutical space is a unique niche within the nutraceutical industry promoting products that benefit the immunologicalhealth.</li>
      <li>The Canadian nutraceuticals market (which includes immunoceuticals) is expected to grow 5.62% annually during the period 2019-2024.</li>
      <li>Competitors include large pharmaceutical companies and smaller natural product companies with primary distribution channels being health food stores, supermarkets, convenience stores, and direct-to-consumer companies.</li>
    </ul>
  </div>

  <div class="abs plan">
    <div class="tag">
      <span class="tag__icon"><svg width="16" height="16" viewBox="0 0 16 16" fill="none" stroke="#ec2227" stroke-width="1.1"><rect x="1.5" y="2" width="8" height="11" rx="1"/><path d="M3.5 5h4M3.5 7.5h4M3.5 10h2.5"/><circle cx="12" cy="11" r="2.6"/></svg></span>
      <span class="tag__label">Business Plan</span>
    </div>
    <ul>
      <li>The mandate of the company is to perform research, provide resources and services, and develop, test and market products in the immunoceutical space.</li>
      <li>The company will specialize in products and systems that promote human and animal health and wellbeing.</li>
      <li>It will also strive to educate the public on how immunoceuticals can bolster natural immunity and thereby help prevent and treat disorders associated with sub-optimal immunity.</li>
      <li>Currently under development: a home-test kit for Vitamin D levels for mass distribution</li>
    </ul>
    <div class="tag fin">
      <span class="tag__icon"><svg width="16" height="16" viewBox="0 0 16 16" fill="none" stroke="#ec2227" stroke-width="1.1"><rect x="1.5" y="2" width="13" height="10" rx="1"/><path d="M4 10V7M7 10V5M10 10V8M12.5 10V4M8 12v2.5"/></svg></span>
      <span class="tag__label" style="width:100px">Financial Projections</span>
    </div>
    <ul class="fin-list">
      <li>Initial start-up lab equipment costs: <span class="money">$325,000</span></li>
      <li>First 6-month operational budget: <span class="money">$340,000</span></li>
      <li>First 6-month revenue target is: <span class="money">$200,000</span></li>
      <li>Start-up date target: <span class="money">July 1, 2022</span></li>
    </ul>
  </div>

  <div class="abs contact">
    NutriVance Contact Information:<br>
    <span class="contact__name">Dr. Martin Hale <small>(Board Chair)</small></span><br>
    martin.hale@nutrivance-mail.com
    <div class="contact__phone">555-014-2290</div>
  </div>
  <div class="abs request">Complete business plan available upon request</div>
</section>

</body>
</html>
```